Hadley & Partners, LLC Business Card 2016

We need a new business card design for a very important trade show coming up.

We are a compliance Consulting Firm. Our clients are stock brokerage firms and investment advisers.

I would like our logo on both sides of the card.

Info in the front of the card shold include:

Logo
First & Last Name
Title
Office #
Cell #
Email
Company Address (42 W. Calloway St., Suite 300 Larkfield, CO 91417

Back of the card should include the logo and url: www.hadleypartnersgroup.com

Target Market(s)

Stock Brokerage Firms and Investment Advisers

Industry/Entity Type

Financial Service

Contact Information for Business Card

Marcus J. Pellew
President
42 W. Calloway St., Suite 300
Larkfield, CO 91417
O 555.210.0147 ext. 204
C 555.310.0193
Email: marcus@hadleypartnersgroup.com
www.hadleypartnersgroup.com

Requirements
Nice to have
• The back of the card could be black with the logo with the white letters.
• I do want the front of the card to at least have the color logo with the black "Hadley & Partners Lettering.

```html
<!DOCTYPE html>
<html lang="en">
<head>
<meta charset="utf-8">
<title>Hadley &amp; Partners — Business Card</title>
<link rel="stylesheet" href="https://fonts.googleapis.com/css2?family=Questrial&display=swap">
<style>
  :root {
    --backdrop: #3b3b3b;
    --card-light: #f4f4f4;
    --card-light-edge: #e2e2e2;
    --card-dark: #2a2a2a;
    --card-dark-edge: #161616;
    --ink: #333333;
    --ink-soft: #555555;
    --accent: #b3221f;
    --rule: #8a8a98;
    --white: #ffffff;
  }
  * { margin: 0; padding: 0; box-sizing: border-box; }
  html, body { width: 1200px; height: 960px; overflow: hidden; }
  body {
    background: var(--backdrop);
    font-family: "Questrial", "Century Gothic", sans-serif;
    color: var(--ink);
    position: relative;
  }
  .card {
    position: absolute;
    left: 258px;
    width: 677px;
    height: 374px;
  }
  .card--front {
    top: 83px;
    background: radial-gradient(ellipse at 45% 35%, var(--white) 0%, var(--card-light) 55%, var(--card-light-edge) 100%);
  }
  .card--back {
    top: 503px;
    background: radial-gradient(ellipse at 50% 40%, var(--card-dark) 0%, #222 60%, var(--card-dark-edge) 100%);
  }
  .brand {
    position: absolute;
    display: flex;
    align-items: center;
    gap: 16px;
  }
  .brand__mark {
    width: 52px;
    height: 52px;
    background: var(--accent);
  }
  .brand__name {
    font-size: 40px;
    font-weight: 400;
    letter-spacing: 1px;
    white-space: nowrap;
  }
  .card--front .brand { left: 42px; top: 58px; }
  .card--front .brand__name { color: var(--ink); }
  .card--back .brand { left: 50%; top: 160px; transform: translateX(-50%); }
  .card--back .brand__name { color: var(--white); }

  .person { position: absolute; left: 40px; top: 185px; right: 42px; }
  .person__name {
    color: var(--accent);
    font-size: 21px;
    font-weight: 400;
    letter-spacing: 0.5px;
    text-transform: uppercase;
  }
  .person__title-row { display: flex; align-items: center; gap: 10px; margin-top: 2px; }
  .person__title { font-size: 15px; color: var(--ink); }
  .person__rule { flex: 1; height: 2px; background: var(--rule); margin-top: 4px; }

  .contact {
    position: absolute;
    left: 40px;
    top: 267px;
    list-style: none;
    font-size: 15px;
    line-height: 19px;
  }
  .contact li { display: flex; align-items: center; gap: 10px; }
  .contact svg { width: 14px; height: 14px; fill: var(--accent); flex: none; }
  .accent { color: var(--accent); }

  .address {
    position: absolute;
    left: 396px;
    top: 304px;
    font-size: 15px;
    line-height: 19px;
    font-style: normal;
    color: var(--ink-soft);
  }
  .back-url {
    position: absolute;
    left: 0; right: 0;
    top: 332px;
    text-align: center;
    font-size: 15px;
    color: #dddddd;
  }
</style>
</head>
<body>
  <section class="card card--front" aria-label="Card front">
    <div class="brand">
      <span class="brand__mark"></span>
      <span class="brand__name">Hadley &amp; Partners</span>
    </div>

    <div class="person">
      <h1 class="person__name">Marcus J. Pellew</h1>
      <div class="person__title-row">
        <span class="person__title">President</span>
        <span class="person__rule"></span>
      </div>
    </div>

    <ul class="contact">
      <li>
        <svg viewBox="0 0 14 14" aria-hidden="true"><rect x="1" y="1" width="4" height="12" rx="1"/><rect x="6" y="3" width="7" height="10" rx="1"/></svg>
        555.210.0147 ext. 204
      </li>
      <li>
        <svg viewBox="0 0 14 14" aria-hidden="true"><path d="M3 1l2.5 3-1.5 1.5c.8 1.8 2.2 3.2 4 4L9.5 8 13 10.5 11.5 13C6 13 1 8 1 2.5z"/></svg>
        555.310.0193
      </li>
      <li>
        <svg viewBox="0 0 14 14" aria-hidden="true"><path d="M1 3h12v1L7 8 1 4z"/><path d="M1 5.5l6 4 6-4V11H1z"/></svg>
        marcus@hadleypartnersgroup.com
      </li>
      <li>
        <svg viewBox="0 0 14 14" aria-hidden="true"><circle cx="7" cy="7" r="5.5" fill="none" stroke="#b3221f" stroke-width="1.4"/><path d="M1.5 7h11M7 1.5c-2 2-2 9 0 11M7 1.5c2 2 2 9 0 11" fill="none" stroke="#b3221f" stroke-width="1.2"/></svg>
        <span>www.<span class="accent">hadleypartnersgroup</span>.com</span>
      </li>
    </ul>

    <address class="address">
      42 W. Calloway St., Suite 300<br>
      Larkfield, CO 91417
    </address>
  </section>

  <section class="card card--back" aria-label="Card back">
    <div class="brand">
      <span class="brand__mark"></span>
      <span class="brand__name">Hadley &amp; Partners</span>
    </div>
    <p class="back-url">www.<span class="accent">hadleypartnersgroup</span>.com</p>
  </section>
</body>
</html>
```